4 x Designs Required

Hi There,
I require 4 x different designs to be made for 4 new brands of mine however they can be quite interchangeable. HR Plinko and Marketing Plinko can be similar just with a difference in colour. The same goes for the Bulletin brands. This means there are ultimately two designs that need perfecting.

There must be a click here CTA on the banner somewhere. :-)

I require the banners in 728x90 format and 960x90 please.

Please use strap lines on the banners such as:
Essential Whitepapers for HR Professionals
Essential Whitepapers for Marketing Professionals
Your No.1 Whitepaper Resource

The brand names:
HR Plinko
Marketing Plinko
HR Gazettor
Marketing Gazettor

Examples attached.

```html
<!DOCTYPE html>
<html lang="en">
<head>
<meta charset="utf-8">
<title>Whitepaper Banner Set</title>
<link rel="stylesheet" href="https://fonts.googleapis.com/css2?family=Poppins:wght@700;800;900&display=swap">
<style>
:root{
  --page:#e3a0e4;
  --white:#ffffff;
  --green:#22b04b;
  --green-dark:#1c8f3d;
  --cyan:#17d8ea;
  --cyan-dark:#0fb6c6;
  --tan:#c99b6b;
  --ink:#0c1722;
  --gazettor-a:#07131d;
  --gazettor-b:#173d5e;
  --plinko-a:#17264a;
  --plinko-b:#1e4c7c;
  --mkt-gazettor:#0a1b2c;
  --mkt-plinko:#2a2123;
}
*{box-sizing:border-box;margin:0;padding:0}
html,body{width:1043px;height:1200px;overflow:hidden}
body{background:var(--page);position:relative;font-family:'Poppins',Arial,sans-serif;font-weight:800;color:var(--white)}
.banner{position:absolute;display:flex;align-items:center;overflow:hidden;text-transform:uppercase;letter-spacing:-0.2px}
.col-left{left:71px;width:379px;height:46px}
.col-right{left:474px;width:506px;height:47px}

.hr-gazettor{background:linear-gradient(90deg,var(--gazettor-a) 0%,#0d2236 35%,var(--gazettor-b) 100%)}
.hr-plinko{background:linear-gradient(100deg,var(--plinko-a) 0%,#1a3560 50%,var(--plinko-b) 100%)}
.mkt-gazettor{background:var(--mkt-gazettor)}
.mkt-plinko{background:var(--mkt-plinko)}

.brand{flex:none;padding-left:9px;line-height:1;white-space:nowrap}
.brand-stack span{display:block}
.strap{flex:1;text-align:center;line-height:1.15;white-space:nowrap}
.strap .line{display:block}
.accent-green .accent{color:var(--green)}
.accent-cyan .accent{color:var(--cyan)}
.accent-tan .accent{color:var(--tan)}
.brand-tan{color:var(--tan)}

.cta{flex:none;display:flex;align-items:center;justify-content:center;border-radius:999px;white-space:nowrap;line-height:1;margin-right:8px}
.cta-green{background:var(--green);box-shadow:0 2px 0 var(--green-dark);color:var(--white)}
.cta-cyan{background:var(--cyan);box-shadow:0 2px 0 var(--cyan-dark);color:var(--plinko-a)}
.cta-sm{width:68px;height:19px;font-size:8.5px}
.cta-lg{width:122px;height:34px;font-size:15.5px}
.cta-md{width:120px;height:33px;font-size:15.5px}
.cta-tan{align-self:stretch;margin:0;background:var(--tan);color:var(--ink);border-radius:26px 0 0 26px;flex-direction:column;font-size:12.5px;line-height:1}
.col-left .cta-tan{width:49px}
.col-right .cta-tan{width:54px;font-size:13px}

.arrow{flex:none;width:26px;height:14px;margin-right:6px}
.arrow-lg{width:40px;height:18px}
</style>
</head>
<body>

<!-- HR Gazettor, 728 -->
<div class="banner hr-gazettor col-left" style="top:94px">
  <div class="brand" style="font-size:13px">HR Gazettor</div>
  <p class="strap accent-green" style="font-size:13.5px"><span class="line"><span class="accent">Your No.1</span> Whitepaper</span><span class="line"><span class="accent">Resource</span></span></p>
  <a class="cta cta-green cta-sm">Click Here</a>
</div>
<div class="banner hr-gazettor col-left" style="top:158px">
  <div class="brand" style="font-size:13px">HR Gazettor</div>
  <p class="strap" style="font-size:13.5px"><span class="line">Your No.1 Whitepaper</span><span class="line">Resource</span></p>
  <a class="cta cta-green cta-sm">Click Here</a>
</div>
<div class="banner hr-gazettor col-left" style="top:222px">
  <div class="brand" style="font-size:13px">HR Gazettor</div>
  <p class="strap accent-green" style="font-size:10px"><span class="accent">Your No.1</span> Whitepaper <span class="accent">Resource</span></p>
  <a class="cta cta-green cta-sm">Click Here</a>
</div>
<div class="banner hr-gazettor col-left" style="top:286px">
  <div class="brand" style="font-size:13px">HR Gazettor</div>
  <p class="strap" style="font-size:10px">Your No.1 Whitepaper Resource</p>
  <a class="cta cta-green cta-sm">Click Here</a>
</div>

<!-- HR Plinko, 728 -->
<div class="banner hr-plinko col-left" style="top:350px">
  <div class="brand" style="font-size:20px">HR Plinko</div>
  <p class="strap accent-cyan" style="font-size:9.5px"><span class="line"><span class="accent">Essential</span> Whitepapers</span><span class="line"><span class="accent">For HR Professionals</span></span></p>
  <svg class="arrow" viewBox="0 0 26 14" aria-hidden="true"><path d="M1 11 H8 C4 11 4 5 10 5 C15 4 20 4 24 3 M21 1 L24 3 L21 5" fill="none" stroke="#fff" stroke-width="0.9"/></svg>
  <a class="cta cta-cyan cta-sm">Click Here</a>
</div>
<div class="banner hr-plinko col-left" style="top:414px">
  <div class="brand" style="font-size:20px">HR Plinko</div>
  <p class="strap" style="font-size:9.5px"><span class="line">Essential Whitepapers</span><span class="line">For HR Professionals</span></p>
  <svg class="arrow" viewBox="0 0 26 14" aria-hidden="true"><path d="M1 11 H8 C4 11 4 5 10 5 C15 4 20 4 24 3 M21 1 L24 3 L21 5" fill="none" stroke="#fff" stroke-width="0.9"/></svg>
  <a class="cta cta-cyan cta-sm">Click Here</a>
</div>
<div class="banner hr-plinko col-left" style="top:478px">
  <div class="brand" style="font-size:14px;padding-left:6px">HR Plinko</div>
  <p class="strap accent-cyan" style="font-size:7.4px"><span class="accent">Essential</span> Whitepapers <span class="accent">For HR Professionals</span></p>
  <a class="cta cta-cyan cta-sm">Click Here</a>
</div>
<div class="banner hr-plinko col-left" style="top:542px">
  <div class="brand" style="font-size:14px;padding-left:6px">HR Plinko</div>
  <p class="strap" style="font-size:7.4px">Essential Whitepapers For HR Professionals</p>
  <a class="cta cta-cyan cta-sm">Click Here</a>
</div>

<!-- Marketing Gazettor, 728 -->
<div class="banner mkt-gazettor col-left" style="top:611px">
  <div class="brand brand-stack" style="font-size:11px"><span>Marketing</span><span>Gazettor</span></div>
  <p class="strap accent-green" style="font-size:13.5px"><span class="line"><span class="accent">Your No.1</span> Whitepaper</span><span class="line"><span class="accent">Resource</span></span></p>
  <a class="cta cta-green cta-sm">Click Here</a>
</div>
<div class="banner mkt-gazettor col-left" style="top:675px">
  <div class="brand brand-stack" style="font-size:11px"><span>Marketing</span><span>Gazettor</span></div>
  <p class="strap" style="font-size:13.5px"><span class="line">Your No.1 Whitepaper</span><span class="line">Resource</span></p>
  <a class="cta cta-green cta-sm">Click Here</a>
</div>
<div class="banner mkt-gazettor col-left" style="top:739px">
  <div class="brand brand-stack" style="font-size:11px"><span>Marketing</span><span>Gazettor</span></div>
  <p class="strap accent-green" style="font-size:10px"><span class="accent">Your No.1</span> Whitepaper <span class="accent">Resource</span></p>
  <a class="cta cta-green cta-sm">Click Here</a>
</div>
<div class="banner mkt-gazettor col-left" style="top:803px">
  <div class="brand brand-stack" style="font-size:11px"><span>Marketing</span><span>Gazettor</span></div>
  <p class="strap" style="font-size:10px">Your No.1 Whitepaper Resource</p>
  <a class="cta cta-green cta-sm">Click Here</a>
</div>

<!-- Marketing Plinko, 728 -->
<div class="banner mkt-plinko col-left" style="top:868px">
  <div class="brand brand-tan" style="font-size:11px">Marketing Plinko</div>
  <p class="strap accent-tan" style="font-size:8.5px"><span class="line"><span class="accent">Essential</span> Whitepapers</span><span class="line"><span class="accent">For Marketing Professionals</span></span></p>
  <svg class="arrow" viewBox="0 0 26 14" aria-hidden="true"><path d="M1 11 H8 C4 11 4 5 10 5 C15 4 20 4 24 3 M21 1 L24 3 L21 5" fill="none" stroke="#fff" stroke-width="0.9"/></svg>
  <a class="cta cta-tan"><span>Click</span><span>Here</span></a>
</div>
<div class="banner mkt-plinko col-left" style="top:932px">
  <div class="brand brand-tan" style="font-size:11px">Marketing Plinko</div>
  <p class="strap" style="font-size:8.5px"><span class="line">Essential Whitepapers</span><span class="line">For Marketing Professionals</span></p>
  <svg class="arrow" viewBox="0 0 26 14" aria-hidden="true"><path d="M1 11 H8 C4 11 4 5 10 5 C15 4 20 4 24 3 M21 1 L24 3 L21 5" fill="none" stroke="#fff" stroke-width="0.9"/></svg>
  <a class="cta cta-tan"><span>Click</span><span>Here</span></a>
</div>
<div class="banner mkt-plinko col-left" style="top:996px">
  <div class="brand brand-tan" style="font-size:7px">Marketing Plinko</div>
  <p class="strap accent-tan" style="font-size:6.6px"><span class="accent">Essential</span> Whitepapers <span class="accent">For Marketing Professionals</span></p>
  <a class="cta cta-tan"><span>Click</span><span>Here</span></a>
</div>
<div class="banner mkt-plinko col-left" style="top:1060px">
  <div class="brand brand-tan" style="font-size:7px">Marketing Plinko</div>
  <p class="strap" style="font-size:6.6px">Essential Whitepapers For Marketing Professionals</p>
  <a class="cta cta-tan"><span>Click</span><span>Here</span></a>
</div>

<!-- HR Gazettor, 960 -->
<div class="banner hr-gazettor col-right" style="top:96px">
  <div class="brand" style="font-size:13px;padding-left:10px">HR Gazettor</div>
  <p class="strap accent-green" style="font-size:16px"><span class="line"><span class="accent">Your No.1</span> Whitepaper</span><span class="line"><span class="accent">Resource</span></span></p>
  <a class="cta cta-green cta-lg">Click Here</a>
</div>
<div class="banner hr-gazettor col-right" style="top:161px">
  <div class="brand" style="font-size:13px;padding-left:10px">HR Gazettor</div>
  <p class="strap" style="font-size:16px"><span class="line">Your No.1 Whitepaper</span><span class="line">Resource</span></p>
  <a class="cta cta-green cta-lg">Click Here</a>
</div>
<div class="banner hr-gazettor col-right" style="top:225px">
  <div class="brand" style="font-size:13px;padding-left:10px">HR Gazettor</div>
  <p class="strap accent-green" style="font-size:15.5px"><span class="accent">Your No.1</span> Whitepaper <span class="accent">Resource</span></p>
  <a class="cta cta-green cta-sm">Click Here</a>
</div>
<div class="banner hr-gazettor col-right" style="top:289px">
  <div class="brand" style="font-size:13px;padding-left:10px">HR Gazettor</div>
  <p class="strap" style="font-size:15.5px">Your No.1 Whitepaper Resource</p>
  <a class="cta cta-green cta-sm">Click Here</a>
</div>

<!-- HR Plinko, 960 -->
<div class="banner hr-plinko col-right" style="top:353px">
  <div class="brand" style="font-size:21px;padding-left:12px">HR Plinko</div>
  <p class="strap accent-cyan" style="font-size:14px"><span class="line"><span class="accent">Essential</span> Whitepapers</span><span class="line"><span class="accent">For HR Professionals</span></span></p>
  <svg class="arrow arrow-lg" viewBox="0 0 26 14" aria-hidden="true"><path d="M1 11 H8 C4 11 4 5 10 5 C15 4 20 4 24 3 M21 1 L24 3 L21 5" fill="none" stroke="#fff" stroke-width="0.8"/></svg>
  <a class="cta cta-cyan cta-md">Click Here</a>
</div>
<div class="banner hr-plinko col-right" style="top:415px">
  <div class="brand" style="font-size:21px;padding-left:12px">HR Plinko</div>
  <p class="strap" style="font-size:14px"><span class="line">Essential Whitepapers</span><span class="line">For HR Professionals</span></p>
  <svg class="arrow arrow-lg" viewBox="0 0 26 14" aria-hidden="true"><path d="M1 11 H8 C4 11 4 5 10 5 C15 4 20 4 24 3 M21 1 L24 3 L21 5" fill="none" stroke="#fff" stroke-width="0.8"/></svg>
  <a class="cta cta-cyan cta-md">Click Here</a>
</div>
<div class="banner hr-plinko col-right" style="top:481px">
  <div class="brand" style="font-size:21px;padding-left:12px">HR Plinko</div>
  <p class="strap accent-cyan" style="font-size:10.8px"><span class="accent">Essential</span> Whitepapers <span class="accent">For HR Professionals</span></p>
  <a class="cta cta-cyan cta-sm">Click Here</a>
</div>
<div class="banner hr-plinko col-right" style="top:545px">
  <div class="brand" style="font-size:21px;padding-left:12px">HR Plinko</div>
  <p class="strap" style="font-size:10.8px">Essential Whitepapers For HR Professionals</p>
  <a class="cta cta-cyan cta-sm">Click Here</a>
</div>

<!-- Marketing Gazettor, 960 -->
<div class="banner mkt-gazettor col-right" style="top:612px">
  <div class="brand" style="font-size:11px;padding-left:10px">Marketing Gazettor</div>
  <p class="strap accent-green" style="font-size:15.5px"><span class="line"><span class="accent">Your No.1</span> Whitepaper</span><span class="line"><span class="accent">Resource</span></span></p>
  <a class="cta cta-green cta-lg" style="width:117px">Click Here</a>
</div>
<div class="banner mkt-gazettor col-right" style="top:674px">
  <div class="brand" style="font-size:11px;padding-left:10px">Marketing Gazettor</div>
  <p class="strap" style="font-size:15.5px"><span class="line">Your No.1 Whitepaper</span><span class="line">Resource</span></p>
  <a class="cta cta-green cta-lg" style="width:117px">Click Here</a>
</div>
<div class="banner mkt-gazettor col-right" style="top:740px">
  <div class="brand" style="font-size:11px;padding-left:10px">Marketing Gazettor</div>
  <p class="strap accent-green" style="font-size:13px"><span class="accent">Your No.1</span> Whitepaper <span class="accent">Resource</span></p>
  <a class="cta cta-green cta-sm">Click Here</a>
</div>
<div class="banner mkt-gazettor col-right" style="top:806px">
  <div class="brand" style="font-size:11px;padding-left:10px">Marketing Gazettor</div>
  <p class="strap" style="font-size:13px">Your No.1 Whitepaper Resource</p>
  <a class="cta cta-green cta-sm">Click Here</a>
</div>

<!-- Marketing Plinko, 960 -->
<div class="banner mkt-plinko col-right" style="top:870px">
  <div class="brand brand-tan" style="font-size:11px">Marketing Plinko</div>
  <p class="strap accent-tan" style="font-size:13.5px"><span class="line"><span class="accent">Essential</span> Whitepapers</span><span class="line"><span class="accent">For Marketing Professionals</span></span></p>
  <svg class="arrow arrow-lg" viewBox="0 0 26 14" aria-hidden="true"><path d="M1 11 H8 C4 11 4 5 10 5 C15 4 20 4 24 3 M21 1 L24 3 L21 5" fill="none" stroke="#fff" stroke-width="0.8"/></svg>
  <a class="cta cta-tan"><span>Click</span><span>Here</span></a>
</div>
<div class="banner mkt-plinko col-right" style="top:933px">
  <div class="brand brand-tan" style="font-size:11px">Marketing Plinko</div>
  <p class="strap" style="font-size:13.5px"><span class="line">Essential Whitepapers</span><span class="line">For Marketing Professionals</span></p>
  <svg class="arrow arrow-lg" viewBox="0 0 26 14" aria-hidden="true"><path d="M1 11 H8 C4 11 4 5 10 5 C15 4 20 4 24 3 M21 1 L24 3 L21 5" fill="none" stroke="#fff" stroke-width="0.8"/></svg>
  <a class="cta cta-tan"><span>Click</span><span>Here</span></a>
</div>
<div class="banner mkt-plinko col-right" style="top:996px">
  <div class="brand brand-tan" style="font-size:11px">Marketing Plinko</div>
  <p class="strap accent-tan" style="font-size:9.8px"><span class="accent">Essential</span> Whitepapers <span class="accent">For Marketing Professionals</span></p>
  <a class="cta cta-tan"><span>Click</span><span>Here</span></a>
</div>
<div class="banner mkt-plinko col-right" style="top:1060px">
  <div class="brand brand-tan" style="font-size:11px">Marketing Plinko</div>
  <p class="strap" style="font-size:9.8px">Essential Whitepapers For Marketing Professionals</p>
  <a class="cta cta-tan"><span>Click</span><span>Here</span></a>
</div>

</body>
</html>
```